Professional BIO Template with photo and logo

Hello,
I need a professional Bio template developed via Microsoft WORD ASAP!!!!! I would like to just be able to add the text I need to add. So resize-able text boxes. Potentially able to adjust the font. These are the things I need added it to include.
Head shot (attached)
Text Box for Name
Text Box for phone number
Text box for email
KTW Logo (attached)
Maybe a blue banner at the top or some background boxes that are blue or grey. Here are the pantone colors that our company uses.

CORE COLOR
100c 91m 17y 6k 38r 58g 128b Hex #263A80 Pantone 7687 C

CORE CONTRAST COLOR
36c 29m 28y 0k 168r 168g 170b Hex #669999 Pantone Cool Gray 6C

I also attached some examples of what we have been looking at. Instead of green add the blue...instead of black maybe just be white.

Thank you

```html
<!DOCTYPE html>
<html lang="en">
<head>
<meta charset="utf-8">
<title>Dana Whitfield – Bio</title>
<link rel="stylesheet" href="https://fonts.googleapis.com/css2?family=Anton&family=Roboto:wght@400;500;700&display=swap">
<style>
  :root {
    --brand-purple: #372770;
    --panel-tint: #f3f0fd;
    --ink: #161616;
    --white: #ffffff;
    --accent-circle: #554a88;
    --skyline-tone: #4d4184;
    --photo-tone-a: #5c5d60;
    --photo-tone-b: #3a3b3e;
  }
  * { box-sizing: border-box; margin: 0; padding: 0; }
  html, body { width: 848px; height: 1200px; overflow: hidden; background: var(--white); }
  body { font-family: "Roboto", Arial, sans-serif; position: relative; }

  .bio-sheet {
    position: absolute; left: 15px; top: 15px; width: 820px; height: 1172px;
    background: var(--brand-purple); overflow: hidden;
  }
  .intro-panel {
    position: absolute; left: 7px; top: 7px; width: 806px; height: 393px;
    background: var(--panel-tint);
  }
  .headshot {
    position: absolute; left: 16px; top: 17px; width: 366px; height: 359px;
    background: var(--white); padding: 3px;
    box-shadow: 0 0 5px rgba(55, 39, 112, 0.25);
  }
  .headshot-fill {
    width: 100%; height: 100%;
    background: radial-gradient(ellipse at 50% 40%, var(--photo-tone-a), var(--photo-tone-b));
  }
  .intro-text { position: absolute; left: 431px; top: 43px; width: 356px; }
  .person-name {
    font-family: "Anton", Impact, sans-serif; font-weight: 400;
    font-size: 53px; line-height: 1; color: var(--brand-purple); letter-spacing: -0.3px;
  }
  .intro-summary {
    margin-top: 13px; font-size: 10.2px; line-height: 17.2px;
    color: var(--ink); text-align: justify;
  }
  .contact-row { position: absolute; left: 431px; display: flex; align-items: center; }
  .contact-row.phone { top: 246px; }
  .contact-row.email { top: 311px; }
  .contact-icon {
    width: 36px; height: 36px; border-radius: 50%;
    background: var(--brand-purple); display: flex; align-items: center; justify-content: center;
  }
  .contact-details { margin-left: 17px; }
  .contact-label { font-size: 10.8px; font-weight: 700; color: var(--ink); line-height: 1.1; }
  .contact-value { font-size: 17px; color: var(--brand-purple); line-height: 1.2; }
  .phone .contact-value { font-weight: 700; letter-spacing: 0.4px; }
  .email .contact-value { font-weight: 500; }

  .brand-mark {
    position: absolute; left: 627px; top: 416px; width: 152px; height: 117px;
    display: flex; align-items: center; justify-content: center;
    font-family: "Roboto", Arial, sans-serif; font-weight: 700;
    font-size: 42px; color: var(--white); letter-spacing: 3px;
  }
  .about-title {
    position: absolute; left: 39px; top: 472px;
    font-family: "Anton", Impact, sans-serif; font-weight: 400;
    font-size: 56px; line-height: 1; color: var(--white);
  }
  .about-body { position: absolute; left: 39px; top: 550px; width: 742px; color: var(--white); }
  .about-body p { font-size: 10.2px; line-height: 20.5px; text-align: justify; }
  .about-body p + p { margin-top: 17px; }
  .accent-circle {
    position: absolute; left: 39px; top: 1008px; width: 144px; height: 144px;
    border-radius: 50%; background: var(--accent-circle);
  }
  .skyline-band {
    position: absolute; left: 215px; top: 1007px; width: 400px; height: 165px;
    background: linear-gradient(to top, var(--skyline-tone), rgba(77, 65, 132, 0.35));
  }
</style>
</head>
<body>
<main class="bio-sheet">
  <section class="intro-panel">
    <figure class="headshot">
      <div class="headshot-fill" role="img" aria-label="Head shot portrait of Dana Whitfield"></div>
    </figure>
    <div class="intro-text">
      <h1 class="person-name">DANA WHITFIELD</h1>
      <p class="intro-summary">Sed ut perspiciatis unde omnis iste natus error sit voluptatem accusantium doloremque laudantium, totam rem aperiam, eaque ipsa quae ab illo inventore veritatis et quasi architecto beatae vitae dicta sunt explicabo. Nemo enim ipsam voluptatem quia voluptas sit aspernatur aut odit aut fugit, sed quia consequuntur magni dolores eos qui ratione voluptatem Sed ut perspiciatis unde omnis iste natus error sit voluptatem accusantium doloremque laudantium, totam rem aperiam, eaque ipsa quae</p>
    </div>
    <div class="contact-row phone">
      <span class="contact-icon">
        <svg width="16" height="16" viewBox="0 0 24 24" aria-hidden="true"><path fill="#fff" d="M6.6 10.8a15.2 15.2 0 0 0 6.6 6.6l2.2-2.2c.3-.3.7-.4 1-.2 1.1.4 2.3.6 3.6.6.6 0 1 .4 1 1V20c0 .6-.4 1-1 1A17 17 0 0 1 3 4c0-.6.4-1 1-1h3.5c.6 0 1 .4 1 1 0 1.3.2 2.5.6 3.6.1.3 0 .7-.2 1z"/></svg>
      </span>
      <div class="contact-details">
        <div class="contact-label">PHONE NO :</div>
        <div class="contact-value">+ 1 555 014 2288 , + 1 555 017 3390</div>
      </div>
    </div>
    <div class="contact-row email">
      <span class="contact-icon">
        <svg width="16" height="16" viewBox="0 0 24 24" aria-hidden="true"><rect x="2" y="5" width="20" height="14" rx="2" fill="#fff"/><path d="M2.5 6.5 12 13l9.5-6.5" fill="none" stroke="#372770" stroke-width="1.8"/></svg>
      </span>
      <div class="contact-details">
        <div class="contact-label">EMAIL ADDRESS :</div>
        <div class="contact-value">info@danawhitfield.com</div>
      </div>
    </div>
  </section>

  <div class="brand-mark">KTW</div>

  <h2 class="about-title">ABOUT ME</h2>
  <div class="about-body">
    <p>Sed ut perspiciatis unde omnis iste natus error sit voluptatem accusantium doloremque laudantium, totam rem aperiam, eaque ipsa quae ab illo inventore veritatis et quasi architecto beatae vitae dicta sunt explicabo. Nemo enim ipsam voluptatem quia voluptas sit aspernatur aut odit aut fugit, sed quia consequuntur magni dolores eos qui ratione voluptatem Sed ut perspiciatis unde omnis iste natus error sit voluptatem accusantium doloremque laudantium, totam rem aperiam, eaque ipsa quaeab illo inventore veritatis et quasi architecto beatae vitae dicta sunt explicabo. Nemo enim ipsam voluptatem quia voluptas sit aspernatur aut odit aut fugit, sed quia consequuntur magni dolores eos qui ratione voluptatem Sed ut perspiciatis unde omnis iste natus error sit voluptatem accusantium doloremque laudantium, totam rem aperiam, eaque ipsa quae ab illo inventore veritatis et quasi architecto beatae vitae dicta sunt explicabo. Nemo enim ipsam voluptatem quia voluptas sit aspernatur aut odit aut fugit, sed quia consequuntur magni dolores eos qui ratione voluptatem Sed ut perspiciatis unde omnis iste natus error sit voluptatem accusantium doloremque laudantium, totam rem aperiam, eaque ipsa quaeab illo inventore veritatis et quasi architecto beatae vitae dicta sunt explicabo. Nemo enim ipsam voluptatem quia voluptas sit aspernatur aut odit aut fugit, sed quia consequuntur magni dolores eos qui ratione voluptatem Sed ut perspiciatis unde omnis iste natus error sit voluptatem accusantium doloremque laudantium, totam rem aperiam, eaque ipsa quae ab illo inventore veritatis et quasi architecto beatae vitae dicta sunt explicabo. Nemo enim ipsam voluptatem quia voluptas sit aspernatur aut odit aut fugit, sed quia consequuntur magni dolores eos qui ratione voluptatem Sed ut perspiciatis unde omnis iste natus error sit voluptatem accusantium doloremque laudantium, totam rem aperiam, eaque ipsa quaeab illo inventore veritatis et quasi architecto beatae vitae dicta sunt explicabo. Nemo enim ipsam voluptatem quia voluptas sit aspernatur aut odit aut fugit, sed quia consequuntur magni dolores eos qui ratione voluptatem</p>
    <p>Sed ut perspiciatis unde omnis iste natus error sit voluptatem accusantium doloremque laudantium, totam rem aperiam, eaque ipsa quae ab illo inventore veritatis et quasi architecto beatae vitae dicta sunt explicabo. Nemo enim ipsam voluptatem quia voluptas sit aspernatur aut odit aut fugit, sed quia consequuntur magni dolores eos qui ratione voluptatem Sed ut perspiciatis unde omnis iste natus error sit voluptatem accusantium doloremque laudantium, totam rem aperiam, eaque ipsa quaeab illo inventore veritatis et quasi architecto beatae vitae dicta sunt explicabo. Nemo enim ipsam voluptatem quia voluptas sit aspernatur aut odit aut fugit, sed quia consequuntur magni dolores eos qui ratione voluptatem Sed ut perspiciatis unde omnis iste natus error sit voluptatem accusantium doloremque laudantium, totam rem aperiam, eaque ipsa quae ab illo inventore veritatis et quasi architecto beatae vitae</p>
  </div>
  <div class="accent-circle" aria-hidden="true"></div>
  <div class="skyline-band" role="img" aria-label="Decorative city skyline outline"></div>
</main>
</body>
</html>
```